A3 Poster & DL Flyer Design Project

We need a poster and flyer designed to advertise a Wine, Food and Live music event.
Event title is "Sunlit Vine Gathering" and is put on by Morrow Creek Wines. Date for the event is Sunday 21 April 2013
The outdoor event covers wine, gourmet food and live music
Live music genera is Jazz, Blues, Swing
Updates

Reason: Most of the designs did not meet our requirements only 3 out of 21 have potential but would like to see more

Target Market(s)

25 - 55 wine drinkers with money.

Industry/Entity Type

Event

Requirements
Must have
• Title of the Event "Sunlit Vine Gathering"
Date Sunday 21 April 2013 or be generic where we can write the date on each year.
Camel Logo
Entry is Free
No BYO Alcohol
Must reflect Wine, Food & Live Music

```html
<!DOCTYPE html>
<html lang="en">
<head>
<meta charset="utf-8">
<title>Sunlit Vine Gathering — Poster</title>
<link rel="stylesheet" href="https://fonts.googleapis.com/css2?family=Covered+By+Your+Grace&family=Nunito+Sans:wght@300;400&display=swap">
<style>
  :root {
    --paper: #eef2e6;
    --ink: #111111;
    --cream: #f4f4ea;
    --gingham-deep: rgba(88, 120, 184, 0.62);
    --gingham-mid: rgba(150, 172, 210, 0.38);
    --brand-slate: #7b9aa7;
    --emblem-ink: #1a1a1a;
  }
  * { margin: 0; padding: 0; box-sizing: border-box; }
  html, body { width: 847px; height: 1200px; overflow: hidden; background: var(--paper); }
  .poster {
    position: relative;
    width: 847px;
    height: 1200px;
    background: var(--paper);
    overflow: hidden;
    font-family: "Nunito Sans", Arial, sans-serif;
    color: var(--ink);
  }
  .tablecloth {
    position: absolute;
    inset: 0 0 150px 0;
    background:
      linear-gradient(205deg, var(--gingham-deep) 0%, var(--gingham-mid) 38%, rgba(200, 212, 230, 0.15) 62%, transparent 78%);
  }
  .seal {
    position: absolute;
    left: 411px;
    top: 400px;
    transform: translate(-50%, -50%);
    width: 640px;
    height: 640px;
  }
  .seal svg { position: absolute; inset: 0; }
  .seal-halo { fill: var(--paper); }
  .seal-content {
    position: absolute;
    left: 50%;
    top: 50%;
    transform: translate(-50%, -50%);
    width: 460px;
    padding-top: 36px;
    display: flex;
    flex-direction: column;
    align-items: center;
    color: var(--cream);
    text-align: center;
  }
  .event-title {
    font-family: "Covered By Your Grace", cursive;
    font-weight: 400;
    font-size: 84px;
    line-height: 1.12;
    letter-spacing: 1px;
  }
  .event-tagline {
    font-weight: 300;
    font-size: 32px;
    line-height: 1;
    margin-top: 16px;
    white-space: nowrap;
  }
  .footer-rule {
    position: absolute;
    left: 33px;
    right: 38px;
    top: 1053px;
    border-top: 2px solid var(--ink);
  }
  .host-brand {
    position: absolute;
    left: 36px;
    top: 1081px;
    width: 196px;
    display: flex;
    flex-direction: column;
    gap: 12px;
  }
  .host-brand-mark {
    width: 196px;
    height: 56px;
    background: var(--brand-slate);
  }
  .host-brand-name {
    font-size: 11px;
    letter-spacing: 2.4px;
    text-transform: uppercase;
    color: var(--ink);
    white-space: nowrap;
  }
  .camel-emblem {
    position: absolute;
    left: 312px;
    top: 1081px;
    width: 78px;
    height: 76px;
    background: linear-gradient(180deg, #2a2a2a, var(--emblem-ink));
    opacity: 0.9;
  }
  .event-details {
    position: absolute;
    left: 508px;
    top: 1074px;
    font-size: 25px;
    line-height: 1.4;
    font-weight: 400;
    white-space: nowrap;
  }
</style>
</head>
<body>
  <main class="poster">
    <div class="tablecloth" role="img" aria-label="Blue and white gingham tablecloth pattern running diagonally"></div>

    <section class="seal">
      <svg viewBox="0 0 640 640" aria-hidden="true">
        <circle class="seal-halo" cx="320" cy="320" r="298"/>
        <circle cx="320" cy="320" r="300" fill="none" stroke="var(--ink)" stroke-width="16" stroke-dasharray="12 20"/>
        <circle cx="320" cy="320" r="268" fill="var(--ink)"/>
      </svg>
      <div class="seal-content">
        <h1 class="event-title">Sunlit Vine<br>Gathering</h1>
        <p class="event-tagline">Wine / Food / Live Music</p>
      </div>
    </section>

    <div class="footer-rule"></div>

    <div class="host-brand">
      <div class="host-brand-mark"></div>
      <span class="host-brand-name">Morrow Creek Wines</span>
    </div>

    <div class="camel-emblem" role="img" aria-label="Silhouette emblem of a camel led by a handler"></div>

    <div class="event-details">
      <p>SUNDAY 21 APRIL 2013</p>
      <p>Entry is Free</p>
      <p>No BYO Alcohol</p>
    </div>
  </main>
</body>
</html>
```